Business Card Design for LeafCrest (Farming Devices)

We need Business Cards for our new Company based in Switzerland called "LeafCrest" We develop innovativ products for indoor and outdoor Farming for household and components for vertical farming. Our initial BloomNest gives people the possibility to grow their own food at home all year round. The design should communicate freshness, innovation, health.

```html
<!DOCTYPE html>
<html lang="en">
<head>
<meta charset="utf-8">
<title>LeafCrest Business Card</title>
<link rel="stylesheet" href="https://fonts.googleapis.com/css2?family=Arimo:wght@400;700&display=swap">
<style>
  :root {
    --backdrop: #d8d8d8;
    --card: #ffffff;
    --brand-green: #6cb33f;
    --brand-blue: #1a6fb5;
    --ink: #1a1a1a;
    --band-top: #5a9a12;
    --band-bottom: #a8c408;
  }
  * { box-sizing: border-box; margin: 0; padding: 0; }
  html, body {
    width: 1200px; height: 1200px; overflow: hidden;
    background: var(--backdrop);
    font-family: "Arimo", Arial, sans-serif;
  }
  .canvas { position: relative; width: 1200px; height: 1200px; }
  .card {
    position: absolute;
    width: 716px; height: 439px;
    background: var(--card);
    overflow: hidden;
  }
  .card--front { left: 233px; top: 103px; }
  .card--back { left: 236px; top: 663px; }
  .card__band {
    position: absolute;
    left: 0; right: 0; bottom: 0;
    background: linear-gradient(to bottom, var(--band-top), var(--band-bottom));
  }
  .card--front .card__band { height: 100px; }
  .card--back .card__band { height: 110px; }
  .brand-name {
    position: absolute;
    font-weight: 700;
    font-size: 42px;
    letter-spacing: -0.5px;
    color: var(--brand-green);
    white-space: nowrap;
  }
  .card--front .brand-name { left: 36px; top: 138px; }
  .card--back .brand-name { left: 0; right: 0; top: 168px; text-align: center; }
  .holder { position: absolute; left: 357px; top: 70px; }
  .holder__name { font-weight: 700; font-size: 35px; color: var(--brand-green); line-height: 1; }
  .holder__role { margin-top: 16px; font-size: 21px; color: var(--ink); }
  .contacts { position: absolute; left: 359px; top: 175px; list-style: none; }
  .contacts__item {
    display: flex; align-items: center; gap: 12px;
    font-size: 15.5px; color: var(--ink);
    height: 22px; margin-bottom: 10px;
  }
  .contacts__item:nth-child(3) { margin-bottom: 14px; }
  .contacts__icon { width: 18px; height: 18px; flex: none; }
</style>
</head>
<body>
<main class="canvas">
  <section class="card card--front" aria-label="Business card front">
    <div class="card__band" role="img" aria-label="Green decorative band along the bottom edge"></div>
    <p class="brand-name">LeafCrest</p>
    <div class="holder">
      <h1 class="holder__name">Name Surname</h1>
      <p class="holder__role">Position</p>
    </div>
    <ul class="contacts">
      <li class="contacts__item">
        <svg class="contacts__icon" viewBox="0 0 24 24"><path d="M6.6 2.5c.8-.5 1.7-.3 2.2.5l1.7 2.8c.4.7.3 1.6-.3 2.1l-1.4 1.2c.9 2 2.3 3.6 4.2 4.8l1.3-1.3c.6-.5 1.4-.6 2.1-.2l2.8 1.8c.8.5 1 1.5.5 2.3l-1.2 1.9c-.6.9-1.7 1.3-2.7 1C9.5 17.8 5.5 12.9 4.6 6.3c-.1-1 .3-2 1.2-2.6z" fill="var(--brand-blue)" transform="rotate(-10 12 12)"/></svg>
        <span>+000 000 0000</span>
      </li>
      <li class="contacts__item">
        <svg class="contacts__icon" viewBox="0 0 24 24" fill="none" stroke="var(--brand-blue)" stroke-width="1.8"><rect x="3" y="5.5" width="18" height="13"/><path d="M3 6l9 7 9-7"/></svg>
        <span>yourmail.mail.com</span>
      </li>
      <li class="contacts__item">
        <svg class="contacts__icon" viewBox="0 0 24 24" fill="none" stroke="var(--brand-blue)" stroke-width="1.6"><circle cx="12" cy="12" r="9"/><ellipse cx="12" cy="12" rx="4" ry="9"/><path d="M3 12h18M4.5 7.5h15M4.5 16.5h15"/></svg>
        <span>www.yourwebsite.com</span>
      </li>
      <li class="contacts__item">
        <svg class="contacts__icon" viewBox="0 0 24 24" fill="none" stroke="var(--brand-blue)" stroke-width="1.8"><path d="M12 21.5s-6.5-6.8-6.5-11.5a6.5 6.5 0 0 1 13 0c0 4.7-6.5 11.5-6.5 11.5z"/><circle cx="12" cy="10" r="2.3"/></svg>
        <span>your company adress</span>
      </li>
    </ul>
  </section>

  <section class="card card--back" aria-label="Business card back">
    <div class="card__band" role="img" aria-label="Green decorative band along the bottom edge"></div>
    <p class="brand-name">LeafCrest</p>
  </section>
</main>
</body>
</html>
```